Brivond Technologies business card design

We need a business card designed with our new logo. it would be great if the card could communicate it is a technology based company.

Target Market(s)

system integrators

Industry/Entity Type

technology, IOT

Contact Information for Business Card

Name, designation, Address, telephone number, email address

Requirements
Must have
• logo and company name
Nice to have
• something to do with technology

```html
<!DOCTYPE html>
<html lang="en">
<head>
<meta charset="utf-8">
<title>Brivond Technologies Business Card</title>
<link rel="stylesheet" href="https://fonts.googleapis.com/css2?family=Exo+2:wght@700&family=Poppins:wght@200&display=swap">
<style>
  :root {
    --page: #ffffff;
    --card-dark: #212121;
    --card-mid: #2c2c2c;
    --card-light: #363636;
    --curve-dark: #232323;
    --curve-light: #474747;
    --ink: #ffffff;
    --accent: #f7941d;
  }
  * { margin: 0; padding: 0; box-sizing: border-box; }
  html, body {
    width: 1200px; height: 1200px; overflow: hidden;
    background: var(--page);
  }
  .canvas { position: relative; width: 1200px; height: 1200px; }
  .card {
    position: absolute; left: 183px; width: 827px; height: 495px;
    overflow: hidden;
  }
  .card-front { top: 111px; }
  .card-back { top: 617px; }
  .circuit-texture {
    position: absolute; inset: 0;
    background: linear-gradient(170deg, var(--card-mid) 0%, var(--card-dark) 35%, var(--card-light) 100%);
  }
  .back-curve { position: absolute; inset: 0; }
  .brand {
    position: absolute; display: flex; align-items: center; gap: 18px;
    color: var(--ink);
    font-family: "Exo 2", sans-serif; font-weight: 700;
  }
  .brand-mark { background: var(--accent); flex: none; }
  .brand-name { display: flex; flex-direction: column; line-height: 1; }
  .brand-front { left: 180px; top: 178px; }
  .brand-front .brand-mark { width: 62px; height: 62px; }
  .brand-front .brand-word { font-size: 72px; letter-spacing: 2px; }
  .brand-front .brand-sub { font-size: 22px; letter-spacing: 12.4px; margin-top: 10px; }
  .brand-back { left: 478px; top: 196px; gap: 12px; }
  .brand-back .brand-mark { width: 34px; height: 34px; }
  .brand-back .brand-word { font-size: 39px; letter-spacing: 1px; }
  .brand-back .brand-sub { font-size: 12px; letter-spacing: 6.6px; margin-top: 6px; }
  .contact-list {
    position: absolute; left: 80px; top: 156px; list-style: none;
    font-family: "Poppins", sans-serif; font-weight: 200;
    color: var(--ink); font-size: 25px;
  }
  .contact-item { display: flex; align-items: center; height: 40px; margin-bottom: 22px; }
  .contact-icon { width: 36px; height: 36px; margin-right: 8px; flex: none; }
</style>
</head>
<body>
<main class="canvas">
  <section class="card card-front">
    <div class="circuit-texture" role="img" aria-label="Faint circuit-board line pattern"></div>
    <div class="brand brand-front">
      <span class="brand-mark"></span>
      <div class="brand-name">
        <span class="brand-word">BRIVOND</span>
        <span class="brand-sub">TECHNOLOGIES</span>
      </div>
    </div>
  </section>

  <section class="card card-back">
    <div class="circuit-texture" role="img" aria-label="Faint circuit-board line pattern"></div>
    <svg class="back-curve" viewBox="0 0 827 495" width="827" height="495">
      <defs>
        <linearGradient id="curveFill" x1="0" y1="0" x2="1" y2="1">
          <stop offset="0" stop-color="var(--curve-dark)"/>
          <stop offset="1" stop-color="var(--curve-light)"/>
        </linearGradient>
      </defs>
      <path d="M373,0 L827,0 L827,495 L717,495 C560,490 455,420 420,300 C395,210 385,90 373,0 Z" fill="url(#curveFill)"/>
    </svg>

    <ul class="contact-list">
      <li class="contact-item">
        <svg class="contact-icon" viewBox="0 0 36 36"><path d="M18 3a11 11 0 0 1 11 11c0 6-11 19-11 19S7 20 7 14A11 11 0 0 1 18 3z" fill="#fff"/><circle cx="18" cy="13" r="4.5" fill="#2a2a2a"/></svg>
        <span>harbor220avenue</span>
      </li>
      <li class="contact-item">
        <svg class="contact-icon" viewBox="0 0 36 36" fill="none" stroke="#fff" stroke-width="2.4"><circle cx="18" cy="18" r="15" fill="#fff" stroke="none"/><ellipse cx="18" cy="18" rx="6" ry="15" stroke="#2a2a2a"/><path d="M3 18h30" stroke="#2a2a2a"/></svg>
        <span>www.brivondtech.net</span>
      </li>
      <li class="contact-item">
        <svg class="contact-icon" viewBox="0 0 36 36" fill="none" stroke="#fff" stroke-width="2.2"><rect x="2" y="7" width="32" height="24" rx="2"/><path d="M3 8l12 13q3 3 6 0L33 8z" fill="#fff"/></svg>
        <span>hello@brivondtech.net</span>
      </li>
      <li class="contact-item">
        <svg class="contact-icon" viewBox="0 0 36 36"><path d="M9 4c3 0 4 6 3 8-1 2 4 9 7 9 2-1 6 0 6 3s-4 4-7 3C11 25 5 17 5 10c0-3 2-6 4-6z" fill="#fff"/></svg>
        <span>0425551870</span>
      </li>
    </ul>

    <div class="brand brand-back">
      <span class="brand-mark"></span>
      <div class="brand-name">
        <span class="brand-word">BRIVOND</span>
        <span class="brand-sub">TECHNOLOGIES</span>
      </div>
    </div>
  </section>
</main>
</body>
</html>
```